Design a whitepaper for MARINE TELEMEDICINE SYSTEM

Hi - I would like the attached word document designing into an attractive and engaging white paper to promote the use of telemedicine to the marine industry.

Please read the copy and make the graphics and design fit. Also attaches are our design guidelines.

Target Market(s)

Marine

Industry/Entity Type

Marine

Font styles to use
Sans Serif
Other font styles liked:
• Calibri

Requirements
Must have
• Velbrook Nautical Logo and branding applied (www.velbrook-nautical.example) branding guidelines to follow
• Be engaging and attractive
• Have a great front cover
• images that match the copy
Nice to have
• Marine and medical related imagery
Should not have
• too much text on one page

```html
<!DOCTYPE html>
<html lang="en">
<head>
<meta charset="utf-8">
<title>Telemedicine for the Marine Industry – Whitepaper Cover</title>
<link href="https://fonts.googleapis.com/css2?family=Open+Sans:wght@300;400;600;700&display=swap" rel="stylesheet">
<style>
  :root{
    --backdrop:#e9ecef;
    --navy:#1c2f4a;
    --navy-deep:#16263d;
    --blue:#3b7cb8;
    --blue-mid:#2f6ca6;
    --blue-light:#5a9bd3;
    --pale:#dbe7f2;
    --white:#ffffff;
    --text-soft:#d6e6f5;
  }
  *{box-sizing:border-box;margin:0;padding:0}
  html,body{width:1200px;height:789px;overflow:hidden;background:var(--backdrop);font-family:"Open Sans",sans-serif}
  .spread{position:absolute;left:77px;top:24px;width:1046px;height:740px;display:flex;box-shadow:0 6px 24px rgba(0,0,0,.25)}
  .page{position:relative;width:523px;height:740px;overflow:hidden}

  /* Back cover */
  .back{background:linear-gradient(160deg,var(--blue) 0%,var(--blue-mid) 100%);color:var(--white)}
  .back .ship-visual{position:absolute;left:40px;top:150px;width:330px;height:280px;border-radius:8px;
    background:radial-gradient(ellipse at 50% 50%,rgba(255,255,255,.14),rgba(255,255,255,0) 70%)}
  .back-copy{position:absolute;left:40px;top:60px;width:440px;font-size:9.2px;line-height:1.45;color:var(--text-soft)}
  .back-copy h2{font-size:12px;font-weight:700;color:var(--white);margin:0 0 6px}
  .back-copy p{margin-bottom:18px}
  .refs{list-style:none}
  .refs li{margin-bottom:9px;word-break:break-all}
  .back svg.waves{position:absolute;left:0;top:0}
  .offices{position:absolute;left:40px;top:620px;display:flex;gap:46px;font-size:8.5px;line-height:1.45;color:var(--text-soft)}
  .office h3{font-size:11px;font-weight:400;letter-spacing:.5px;color:var(--white);margin-bottom:4px}
  .office .row{display:flex;gap:6px;align-items:flex-start;margin-top:3px}
  .office .row svg{flex:none;margin-top:2px}
  .office .phone{font-size:9.5px;color:var(--white)}
  .connect{position:absolute;right:28px;top:590px;font-size:9px;color:var(--text-soft);text-align:left}
  .social{display:flex;gap:5px;margin-bottom:6px}
  .social span{width:14px;height:14px;border-radius:50%;background:var(--blue-light)}
  .connect .row{display:flex;gap:5px;align-items:center}

  /* Front cover */
  .front{background:var(--white)}
  .front .sea-photo{position:absolute;left:0;top:0;width:523px;height:600px;
    background:linear-gradient(180deg,#f3f6f9 0%,#d9e3ea 22%,#9fb4c2 38%,#6f8d9d 52%,#7e9a8f 62%,#c9d6db 80%,#e4ebee 100%)}
  .brand{position:absolute;left:50px;top:42px}
  .brand-name{font-size:30px;font-weight:700;color:var(--navy);letter-spacing:-.5px;display:flex;align-items:center;gap:8px}
  .brand-name i{width:12px;height:12px;border-radius:50%;background:var(--blue-light);display:block}
  .tagline{font-size:12px;font-weight:600;color:var(--blue-light);margin-top:2px;letter-spacing:.4px}
  .front svg.waves{position:absolute;left:0;top:0}
  .title{position:absolute;right:34px;top:610px;text-align:right;color:var(--white);font-weight:300;font-size:24px;line-height:1.25}
  .web{position:absolute;right:34px;top:690px;display:flex;align-items:center;gap:6px;color:var(--white);font-size:10.5px}
  .web .rule{width:120px;height:1px;background:rgba(255,255,255,.5);margin-right:4px}
</style>
</head>
<body>
<main class="spread">

  <!-- Back cover -->
  <section class="page back">
    <div class="ship-visual" role="img" aria-label="Faint aerial view of a ship deck blended into the blue background"></div>

    <div class="back-copy">
      <h2>The Future Of Telemedicine</h2>
      <p>Telemedicine has developed over the years and continues to evolve today. Lightweight portable ultrasound devices are being developed, not just for producing images, but with treatment capabilities. The pioneering technology uses high-density ultrasound waves to stop internal bleeding, for example from deep tissue and from internal organs. This could enable a larger proportion of patients at sea to be treated in situ, without the need to be transported to a hospital. The Orbital Research Consortium (ORC) is helping to fund research into the development of robots which could perform medical procedures, such as scans and even surgical operations when controlled remotely by a medical professional.</p>

      <h2>Conclusion</h2>
      <p>In the meantime, making use of the telemedicine services available offers the best opportunity for optimising crew welfare and ensuring compliance with the requirements of the Maritime Labour Convention, to provide healthcare of a standard as close as possible to that provided ashore. It also enables ship owners to keep emergency medical costs to a minimum. This combined with a high level of medical competence in nominated officers, through regular high quality training, will help to deliver greater levels of self sufficiency for managing illness and injury at sea.</p>

      <h2>References</h2>
      <ul class="refs">
        <li>Maritime Labour Convention<br>http://www.maritime-labour.example/documents/convention-2006.pdf</li>
        <li>Harcourt Advisory report: Securing Skilled Crews in Today's Marketplace.</li>
        <li>Meridian Class Register</li>
        <li>MedSea Journal article: Nautical officers at sea: emergency experience and need for medical training (2014)</li>
      </ul>
    </div>

    <svg class="waves" width="523" height="740" viewBox="0 0 523 740" aria-hidden="true">
      <path d="M0,545 C120,585 210,455 330,450 C420,446 470,470 523,440 V740 H0Z" fill="var(--blue-light)"/>
      <path d="M0,560 C130,600 215,475 335,470 C425,466 470,490 523,465 V740 H0Z" fill="#e8eef5"/>
      <path d="M0,572 C135,612 220,488 340,483 C428,480 472,502 523,480 V740 H0Z" fill="var(--navy)"/>
    </svg>

    <div class="connect">
      <div class="social" aria-label="Social channels"><span></span><span></span><span></span><span></span></div>
      <div class="row">
        <svg width="10" height="8" viewBox="0 0 10 8"><rect x=".5" y=".5" width="9" height="7" fill="none" stroke="currentColor"/><path d="M.5,.5 5,4.5 9.5,.5" fill="none" stroke="currentColor"/></svg>
        info@velbrook-nautical.example
      </div>
    </div>

    <div class="offices">
      <div class="office">
        <h3>UK HEAD OFFICE</h3>
        <div>Velbrook Nautical</div>
        <div class="row">
          <svg width="8" height="10" viewBox="0 0 8 10"><path d="M4,10 C1,6 0,5 0,4 A4,4 0 0 1 8,4 C8,5 7,6 4,10Z" fill="currentColor"/><circle cx="4" cy="4" r="1.4" fill="var(--navy)"/></svg>
          <span>14 Harbour Row, Keelside,<br>Dunmore,<br>DN4 7QX</span>
        </div>
        <div class="row phone">
          <svg width="9" height="9" viewBox="0 0 9 9"><path d="M2,0 3.5,2.5 2.5,3.5 C3,5 4,6 5.5,6.5 L6.5,5.5 9,7 8,9 C4,9 0,5 0,1Z" fill="currentColor"/></svg>
          <span>+44 (0)1632 960 418</span>
        </div>
        <div class="row phone">
          <svg width="9" height="9" viewBox="0 0 9 9"><rect x="0" y="3" width="9" height="5" rx="1" fill="currentColor"/><rect x="2" y="0" width="5" height="3" fill="currentColor"/></svg>
          <span>+44 (0)1632 960 527</span>
        </div>
      </div>
      <div class="office">
        <h3>ASIA OFFICE</h3>
        <div class="row">
          <svg width="8" height="10" viewBox="0 0 8 10"><path d="M4,10 C1,6 0,5 0,4 A4,4 0 0 1 8,4 C8,5 7,6 4,10Z" fill="currentColor"/><circle cx="4" cy="4" r="1.4" fill="var(--navy)"/></svg>
          <span>9 Quayline Road<br>Level 6 Tidewater Hub<br>Singapore 000000</span>
        </div>
        <div class="row phone">
          <svg width="9" height="9" viewBox="0 0 9 9"><path d="M2,0 3.5,2.5 2.5,3.5 C3,5 4,6 5.5,6.5 L6.5,5.5 9,7 8,9 C4,9 0,5 0,1Z" fill="currentColor"/></svg>
          <span>+65 6000 2718</span>
        </div>
      </div>
    </div>
  </section>

  <!-- Front cover -->
  <section class="page front">
    <div class="sea-photo" role="img" aria-label="Photograph of a businessman in a suit sitting on a folding beach chair in the shallow surf, working on a laptop, seen from behind"></div>

    <div class="brand">
      <div class="brand-name"><i></i>Velbrook Nautical</div>
      <div class="tagline">Innovative Ship Solutions</div>
    </div>

    <svg class="waves" width="523" height="740" viewBox="0 0 523 740" aria-hidden="true">
      <path d="M0,580 C110,520 200,590 300,545 C400,500 460,450 523,455 V740 H0Z" fill="var(--blue-light)"/>
      <path d="M0,595 C115,540 205,605 305,562 C405,520 462,470 523,475 V740 H0Z" fill="var(--white)"/>
      <path d="M0,612 C120,560 210,622 310,580 C410,540 465,490 523,495 V740 H0Z" fill="var(--navy)"/>
    </svg>

    <h1 class="title">Telemedicine<br>for the Marine Industry</h1>
    <div class="web">
      <span class="rule"></span>
      <svg width="10" height="10" viewBox="0 0 10 10"><circle cx="5" cy="5" r="4.4" fill="none" stroke="currentColor"/><ellipse cx="5" cy="5" rx="2" ry="4.4" fill="none" stroke="currentColor"/><path d="M.6,5H9.4" stroke="currentColor"/></svg>
      www.velbrook-nautical.example
    </div>
  </section>

</main>
</body>
</html>
```